Poster Design Project - Quill Bar and Restaurant

We require a Horse Racing Carnival poster (Tarrawong Autumn Turf Festival) to showcase the offer at our Bar/Restaurant.

The venue is called QUILL. Our website is www.quillbar-example.com.au

The venue is heavily design focused with significant use of strong graphics and logos.

The poster will need to be printed out in AO size.
Updates

Once again, thank you all for participating in this design creation. We are going to list a number of other poster briefs shortly that will require strong quirky/design graphics. I hope you'll all participate.

I am happy to provide individual responses to queries about specific designs and why they have been unsuccessful.

Overall we were really impressed with the quality of the submissions.

Thanks Gavin

Target Market(s)

Our demographic is 25-35 years old

Industry/Entity Type

Restaurant

Requirements
Must have
• The following copy needs to be incorporated into the poster -

QUILL

AUTUMN TURF FESTIVAL 2011

Lantern Day - 29th October 2011
Champagne breakfast from 9am
Buses to and from the track
$15 bus ticket includes redeemable drink voucher
DJ from 8pm until 3am

Tarrawong Plate Eve - 31st October 2011
Drink specials all night
DJ from 8pm until close

Tarrawong Plate Day - 1st November 2011
Big screen racing live on 3 screens
Cocktail and drinks specials all day
DJ from 4pm

Fillies Gala - 3rd November 2011
DJ from 8pm until close

Closing Run - 5th November 2011
The finishing post - Complimentary glass of sparkling with presentation of race entry ticket
DJ's from 9pm until 3am

For further enquiries and to secure your bus tickets please contact Corinne on 84172059.

178 Wexford Lane, Port Delvin Vic 3902
Tel: 84172059
Twitter: @thequillbar
Facebook: Quill Bar and Restaurant
www.quillbar-example.com.au
Should not have
• No cheesy graphics

```html
<!DOCTYPE html>
<html lang="en">
<head>
<meta charset="utf-8">
<title>Quill – Autumn Turf Festival 2011</title>
<link rel="stylesheet" href="https://fonts.googleapis.com/css2?family=Rubik:wght@600;700;800;900&family=Ubuntu:wght@500;700&display=swap">
<style>
  :root {
    --sky-top: #fdeaa6;
    --sky-mid: #fbd36a;
    --sky-bottom: #f6ad2a;
    --stripe: rgba(255, 250, 220, 0.38);
    --race-red: #d8102b;
    --deep-red: #8e0d1c;
    --brown: #6b4412;
    --ink: #3a2410;
    --white: #ffffff;
    --ornament: rgba(205, 150, 40, 0.28);
  }
  * { margin: 0; padding: 0; box-sizing: border-box; }
  html, body { width: 850px; height: 1200px; overflow: hidden; background: var(--sky-bottom); }
  .poster {
    position: relative;
    width: 850px;
    height: 1200px;
    overflow: hidden;
    background:
      repeating-linear-gradient(90deg, transparent 0 62px, var(--stripe) 62px 124px),
      linear-gradient(180deg, var(--sky-top) 0%, var(--sky-mid) 55%, var(--sky-bottom) 100%);
    font-family: "Ubuntu", sans-serif;
    color: var(--ink);
  }
  .ornament-field {
    position: absolute;
    left: 290px; top: 360px;
    width: 560px; height: 460px;
    background: radial-gradient(ellipse at center, var(--ornament) 0%, transparent 70%);
  }
  .venue-name {
    position: absolute;
    left: 0; top: 30px; width: 850px;
    text-align: center;
    font-family: "Rubik", sans-serif;
    font-weight: 900;
    font-size: 170px;
    line-height: 170px;
    letter-spacing: 14px;
    color: var(--brown);
  }
  .festival-title {
    position: absolute;
    left: 0; top: 212px; width: 850px;
    text-align: center;
    font-family: "Rubik", sans-serif;
    font-weight: 800;
    font-size: 74px;
    line-height: 84px;
    color: var(--race-red);
    text-shadow:
      -3px -3px 0 var(--white), 3px -3px 0 var(--white),
      -3px 3px 0 var(--white), 3px 3px 0 var(--white),
      0 -3px 0 var(--white), 0 3px 0 var(--white),
      -3px 0 0 var(--white), 3px 0 0 var(--white),
      6px 6px 0 var(--deep-red);
  }
  .event {
    position: absolute;
    width: 390px;
  }
  .event-name {
    font-family: "Rubik", sans-serif;
    font-weight: 700;
    font-size: 29px;
    line-height: 34px;
    text-transform: uppercase;
    color: var(--race-red);
    white-space: nowrap;
  }
  .event-date {
    font-family: "Rubik", sans-serif;
    font-weight: 600;
    font-size: 30px;
    line-height: 38px;
    color: var(--ink);
    margin-bottom: 4px;
  }
  .event-details { list-style: none; }
  .event-details li {
    position: relative;
    padding-left: 17px;
    font-size: 19px;
    line-height: 23px;
    font-weight: 500;
  }
  .event-details li::before {
    content: "";
    position: absolute;
    left: 2px; top: 9px;
    width: 6px; height: 6px;
    border-radius: 50%;
    background: var(--ink);
  }
  .event--lantern { left: 46px; top: 393px; }
  .event--plate-eve { left: 46px; top: 614px; }
  .event--plate-day { left: 46px; top: 760px; }
  .event--fillies { left: 490px; top: 393px; }
  .event--closing { left: 490px; top: 614px; width: 340px; }

  .race-artwork {
    position: absolute;
    left: 290px; top: 816px;
    width: 560px; height: 384px;
    background:
      radial-gradient(circle at 248px 140px, var(--race-red) 0 145px, transparent 146px),
      linear-gradient(180deg, transparent 70%, rgba(58, 36, 16, 0.35) 100%);
  }
  .enquiry-banner {
    position: absolute;
    left: 0; top: 937px;
    width: 310px; height: 109px;
    background: var(--race-red);
    clip-path: polygon(0 0, 100% 0, 92% 100%, 0 100%);
    color: var(--white);
    padding: 10px 0 0 46px;
  }
  .enquiry-text {
    font-size: 18px;
    line-height: 21px;
    font-weight: 500;
  }
  .enquiry-phone {
    display: flex;
    align-items: center;
    gap: 8px;
    font-family: "Rubik", sans-serif;
    font-weight: 700;
    font-size: 29px;
    line-height: 36px;
  }
  .enquiry-phone svg { width: 26px; height: 24px; }
  .venue-contact {
    position: absolute;
    left: 46px; top: 1075px;
    font-size: 18px;
    line-height: 22px;
    font-weight: 500;
  }
  .social-row {
    display: flex;
    align-items: center;
    gap: 8px;
    margin-top: 2px;
  }
  .social-mark {
    display: inline-block;
    width: 20px; height: 20px;
    background: var(--brown);
    border-radius: 2px;
  }
  .social-row .social-item { display: flex; align-items: center; gap: 6px; margin-right: 10px; }
  .web-address {
    margin-top: 4px;
    font-size: 23px;
    line-height: 28px;
    font-weight: 700;
  }
</style>
</head>
<body>
<main class="poster">
  <div class="ornament-field" role="img" aria-label="Faint gold looping scroll ornament behind the event listings"></div>

  <h1 class="venue-name">QUILL</h1>
  <h2 class="festival-title">AUTUMN TURF<br>FESTIVAL 2011</h2>

  <section class="event event--lantern">
    <h3 class="event-name">Lantern Day</h3>
    <p class="event-date">29th October 2011</p>
    <ul class="event-details">
      <li>Champagne breakfast from 9am</li>
      <li>Buses to and from the track</li>
      <li>$15 bus ticket includes<br>redeemable drink voucher</li>
      <li>DJ from 8pm until 3am</li>
    </ul>
  </section>

  <section class="event event--plate-eve">
    <h3 class="event-name">Tarrawong Plate Eve</h3>
    <p class="event-date">31st October 2011</p>
    <ul class="event-details">
      <li>Drink specials all night</li>
      <li>DJ from 8pm until close</li>
    </ul>
  </section>

  <section class="event event--plate-day">
    <h3 class="event-name">Tarrawong Plate Day</h3>
    <p class="event-date">1st November 2011</p>
    <ul class="event-details">
      <li>Champagne breakfast from 9am</li>
      <li>Big screen racing live on 3 screens</li>
      <li>Cocktail and drinks specials all day</li>
      <li>DJ from 4pm</li>
    </ul>
  </section>

  <section class="event event--fillies">
    <h3 class="event-name">Fillies Gala</h3>
    <p class="event-date">3rd November 2011</p>
    <ul class="event-details">
      <li>Champagne breakfast from 9am</li>
      <li>Buses to and from the track</li>
      <li>$15 bus ticket includes<br>redeemable drink voucher</li>
      <li>DJ from 8pm until close</li>
    </ul>
  </section>

  <section class="event event--closing">
    <h3 class="event-name">Closing Run</h3>
    <p class="event-date">5th November 2011</p>
    <ul class="event-details">
      <li>The finishing post —<br>Complimentary glass of sparkling with presentation of race entry ticket</li>
      <li>DJ's from 9pm until 3am</li>
    </ul>
  </section>

  <div class="race-artwork" role="img" aria-label="Galloping racehorse with jockey in silhouette against a red sun"></div>

  <aside class="enquiry-banner">
    <p class="enquiry-text">For further enquiries and<br>to secure your bus tickets<br>please contact Corinne on</p>
    <p class="enquiry-phone">
      <svg viewBox="0 0 26 24" aria-hidden="true">
        <path d="M3 7 Q13 0 23 7 L21 10 L17 8.5 L16.5 6 Q13 5 9.5 6 L9 8.5 L5 10 Z" fill="#fff"/>
        <rect x="6" y="11" width="14" height="11" rx="2" fill="#fff"/>
        <circle cx="13" cy="16.5" r="2.6" fill="#d8102b"/>
      </svg>
      841.720.59
    </p>
  </aside>

  <footer class="venue-contact">
    <p>178 Wexford Lane, Port Delvin<br>Vic 3902&nbsp; Tel: 84172059</p>
    <div class="social-row">
      <span class="social-item"><span class="social-mark"></span>@thequillbar</span>
      <span class="social-item"><span class="social-mark"></span>Quill Bar and Restaurant</span>
    </div>
    <p class="web-address">www.quillbar-example.com.au</p>
  </footer>
</main>
</body>
</html>
```